Infographic on Rock History (but not Rock-and-Roll, unfortunately)

Looking to create an infographic that tells the story of a giant rock that is featured in the architecture of a friend's mountainside home. I have pics of the rock and a geologist's description. Infographic does not need to tell the entire story with all the details - I am looking for a designer to pick out the most interesting, compelling parts of the rock's history and creatively illustrate it - all while keeping it simple.
The entire mountain range is less than 20 million years old, however, the rock is more than 1.75 billion years old. Not surprisingly, the rocks are quite deformed, folded, tilted, metamorphosed, fractured and weathered. The rocks in the house at Brambleton Drive and Wexley dip about 80 degrees to the southeast.
However, the tilted rocks are quartzite, which happens to be the most physically and chemically resistant rock on earth, made of nearly pure quartz sand grains (chemically equivalent to inert Vitrona glass).
The sand grains themselves were eroded from even older terrains of unknown origin, but likely from rocks near Canada or Siberia, rocks themselves at least 2.3 to 3 billion years old. The sand grains were transported by a river to the margin of our North American continent some 1.75 billion years ago and laid down in sheets of well-sorted sand. That is why the layers look so homogenous, albeit fractured.
Deposition continued and the sandy layers were subsequently buried. Over time the sand turned to sandstone. Around 1.65 billion years ago this margin of North America collided with another continent and buckled the crust extensively forming folds, sheared rock, tilted rock and faults. This is a well-known event in Arizona referred to as the Mazatzal Orogeny (named after the Mazatzal Mountains near Rye, AZ).
The sandstone was metamorphosed into quartzite prior to and during this event, a metamorphic rock. Until the Phoenix Mountains formed ~20 million years ago, the tilted quartzite layers have remained essentially in place, tilted as is, and unweathered for nearly 1.7 billion years, which is hard to imagine, but that’s geology. The quartzite on this part of the Preserve represents the top of a thick sequence of metamorphosed sand, mud and volcanic rocks about 8 to 10 miles thick! Okay, that is hard to imagine.
So to summarize, the rock is 1.75 billion-year-old sandstone, made of even older sand grains of unknown origin, metamorphosed ~1.65 billion years ago, buried for ~1.6 billion years until about ~20 million years ago and presently lay exposed to weathering and erosion, and of course, admiration and fascination.
I plan to end the contest early on Monday, September 9 and 8pm ET. If anyone has a problem with that, please let me know and I will consider keeping it through the 10th.
Highly educated adult business professionals
Architecture

```html
<!DOCTYPE html>
<html lang="en">
<head>
<meta charset="utf-8">
<title>Sandstone Rock</title>
<link href="https://fonts.googleapis.com/css2?family=Signika:wght@300;400;700&display=swap" rel="stylesheet">
<style>
  :root {
    --bg-light: #f6f6f6;
    --bg-dark: #d6d6d6;
    --ink: #2b1a1b;
    --maroon: #3a1718;
    --bar: #2e1315;
    --accent-red: #b10f0e;
    --rule: #4a2426;
    --white: #ffffff;
  }
  html, body {
    margin: 0;
    padding: 0;
    width: 1200px;
    height: 776px;
    overflow: hidden;
  }
  .infographic {
    position: relative;
    width: 1200px;
    height: 776px;
    background: radial-gradient(ellipse at 50% 45%, var(--bg-light) 0%, #ececec 55%, var(--bg-dark) 100%);
    font-family: "Signika", "Segoe UI", sans-serif;
    color: var(--ink);
    overflow: hidden;
  }
  .art {
    position: absolute;
    left: 0;
    top: 0;
  }
  .title {
    position: absolute;
    left: 0;
    width: 1200px;
    top: 22px;
    margin: 0;
    text-align: center;
    font-weight: 700;
    font-size: 54px;
    letter-spacing: -0.5px;
    color: var(--maroon);
  }
  .note {
    position: absolute;
    margin: 0;
    font-weight: 300;
    font-size: 16.5px;
    line-height: 19.5px;
    text-align: center;
    color: var(--ink);
    transform: translateX(-50%);
    white-space: nowrap;
  }
  .note--deformed { left: 224px; top: 178px; }
  .note--top { left: 985px; top: 194px; }
  .note--grain { left: 142px; top: 418px; }
  .note--thick { left: 1016px; top: 486px; }

  .dip-box {
    position: absolute;
    left: 938px;
    top: 301px;
    width: 221px;
    height: 80px;
    background: var(--bar);
    box-sizing: border-box;
  }
  .dip-box__text {
    position: absolute;
    left: 72px;
    top: 25px;
    margin: 0;
    font-weight: 300;
    font-size: 13.5px;
    line-height: 16px;
    color: var(--white);
    text-align: center;
  }

  .tl-label {
    position: absolute;
    margin: 0;
    font-weight: 400;
    font-size: 13.5px;
    line-height: 17.5px;
    font-variant: small-caps;
    text-align: center;
    color: var(--ink);
    transform: translateX(-50%);
    white-space: nowrap;
  }
  .tl-label--eroded { left: 165px; top: 633px; }
  .tl-label--river { left: 356px; top: 623px; }
  .tl-label--collide { left: 488px; top: 623px; }
  .tl-label--range { left: 1124px; top: 623px; }
  .tl-label--total { left: 761px; top: 586px; }

  .tl-date {
    position: absolute;
    top: 725px;
    margin: 0;
    font-weight: 300;
    font-size: 9.5px;
    line-height: 11px;
    font-variant: small-caps;
    text-align: center;
    color: var(--ink);
    transform: translateX(-50%);
    white-space: nowrap;
  }
</style>
</head>
<body>
<main class="infographic">
  <svg class="art" width="1200" height="776" viewBox="0 0 1200 776" aria-hidden="false">
    <defs>
      <linearGradient id="rockFill" x1="0" y1="0" x2="1" y2="1">
        <stop offset="0" stop-color="#5a3a3e"/>
        <stop offset="0.35" stop-color="#6e4a52"/>
        <stop offset="0.6" stop-color="#7a4a3e"/>
        <stop offset="1" stop-color="#4a3a40"/>
      </linearGradient>
      <linearGradient id="groundFill" x1="0" y1="0" x2="0" y2="1">
        <stop offset="0" stop-color="#8a7470"/>
        <stop offset="1" stop-color="#b8aaa8"/>
      </linearGradient>
    </defs>

    <!-- rock photograph area -->
    <g role="img" aria-label="Photograph of the tilted quartzite rock outcrop with near-vertical fractured layers">
      <ellipse cx="600" cy="462" rx="378" ry="88" fill="url(#groundFill)"/>
      <path d="M232 452 C250 380 300 300 360 220 C390 180 410 160 430 148 L600 140 L880 160 C900 170 905 190 880 210 L905 290 C930 340 950 400 965 450 C900 490 760 500 600 500 C430 500 300 490 232 452 Z" fill="url(#rockFill)"/>
    </g>

    <!-- detail insets -->
    <g stroke="var(--white)" stroke-width="4">
      <circle cx="395" cy="200" r="47" fill="#8a5a45" role="img" aria-label="Close-up of folded, fractured rock"/>
      <circle cx="843" cy="210" r="47" fill="#9a7a68" role="img" aria-label="Close-up of quartzite at the top of the sequence"/>
      <circle cx="278" cy="440" r="40" fill="#8e8a74" role="img" aria-label="Close-up of sand grains"/>
      <circle cx="683" cy="452" r="40" fill="#a8aaa2" role="img" aria-label="Close-up of quartzite surface"/>
    </g>

    <!-- callout rules -->
    <g fill="none" stroke="var(--rule)" stroke-width="1.2">
      <polyline points="219,160 219,125 387,125 387,145"/>
      <polyline points="826,152 826,137 986,137 986,176"/>
      <polyline points="137,404 137,363 240,363"/>
      <line x1="690" y1="505" x2="940" y2="505"/>
    </g>

    <!-- dip icon -->
    <g transform="translate(948 309)">
      <rect x="0" y="0" width="201" height="64" fill="none" stroke="var(--white)" stroke-width="1"/>
      <line x1="10" y1="58" x2="60" y2="58" stroke="var(--white)" stroke-width="1.2"/>
      <line x1="10" y1="58" x2="18" y2="8" stroke="var(--white)" stroke-width="1.2"/>
      <path d="M18 8 A52 52 0 0 1 62 58 L48 58 A38 38 0 0 0 20 20 Z" fill="var(--white)"/>
      <path d="M31 58 A21 21 0 0 0 13 38" fill="none" stroke="var(--white)" stroke-width="1"/>
      <text x="30" y="55" fill="var(--white)" font-family="Signika, sans-serif" font-size="9" font-weight="300">80º</text>
    </g>

    <!-- timeline bracket -->
    <g fill="none" stroke="var(--rule)" stroke-width="1">
      <polyline points="353,617 353,600 705,600"/>
      <polyline points="818,600 1167,600 1167,617"/>
      <line x1="296" y1="676" x2="296" y2="690"/>
      <line x1="488" y1="676" x2="488" y2="690"/>
      <line x1="1079" y1="676" x2="1079" y2="690"/>
    </g>

    <!-- timeline bars -->
    <rect x="30" y="690" width="316" height="23" fill="var(--bar)"/>
    <rect x="353" y="690" width="726" height="23" fill="var(--bar)"/>
    <rect x="1079" y="690" width="88" height="23" fill="var(--accent-red)"/>

    <!-- tick marks -->
    <g stroke="var(--rule)" stroke-width="1">
      <line x1="30" y1="713" x2="30" y2="724"/>
      <line x1="296" y1="713" x2="296" y2="724"/>
      <line x1="353" y1="713" x2="353" y2="724"/>
      <line x1="488" y1="713" x2="488" y2="724"/>
      <line x1="1079" y1="713" x2="1079" y2="724"/>
      <line x1="1167" y1="713" x2="1167" y2="724"/>
    </g>
  </svg>

  <h1 class="title">Sandstone Rock</h1>

  <p class="note note--deformed">Deformed Rocks, folded,<br>tilted, metamorphosed,<br>fractured and weathered.</p>
  <p class="note note--top">Quartzites represents the<br>top of a thick.</p>
  <p class="note note--grain">Sandgrain eroded<br>from older terrains of<br>unknown origin.</p>
  <p class="note note--thick">Quartzites are about 8 -10<br>miles thick</p>

  <div class="dip-box">
    <p class="dip-box__text">The rocks are about 80º<br>dip to the southeast.</p>
  </div>

  <p class="tl-label tl-label--total">Total age of the<br>sandstone rock</p>
  <p class="tl-label tl-label--eroded">Eroded from rocks near<br>Canada or Siberia</p>
  <p class="tl-label tl-label--river">Sands grain<br>transported by<br>river</p>
  <p class="tl-label tl-label--collide">North America<br>collide with<br>another continent</p>
  <p class="tl-label tl-label--range">Entire<br>mountain<br>range</p>

  <p class="tl-date" style="left:32px">3 Billion<br>Years Ago</p>
  <p class="tl-date" style="left:296px">2 Billion<br>Years Ago</p>
  <p class="tl-date" style="left:357px">1.75 Billion<br>Years Ago</p>
  <p class="tl-date" style="left:488px">1.65 Billion<br>Years Ago</p>
  <p class="tl-date" style="left:1080px">20 Million<br>Years Ago</p>
  <p class="tl-date" style="left:1167px">Today</p>
</main>
</body>
</html>
```